Sleep Consulting Business

Hello I need a business card design with similar colors to my logo that was created. I help mom/parents whose little ones are having sleep issues. Are you able to recreate the picture with the girl sleeping onto a business card using a picture that I provide. That would be one side with my logo on top and on the other side would the following:
My name (in bigger letters than the rest. maybe written in script
title
email
website
phone
instagram
I have included color Inspo
Full Name, number, email, website, ig page

```html
<!DOCTYPE html>
<html lang="en">
<head>
<meta charset="utf-8">
<title>Hushed Hours – Business Card</title>
<link href="https://fonts.googleapis.com/css2?family=Dancing+Script:wght@600&family=Montserrat:wght@400;500;600&display=swap" rel="stylesheet">
<style>
  :root {
    --backdrop: #c9c9cb;
    --card-white: #fbfaf8;
    --card-black: #0d0c0c;
    --copper: #c98d74;
    --taupe: #7b716c;
    --soft-grey: #b9b4b1;
    --ink-white: #f4f2f0;
  }
  * { margin: 0; padding: 0; box-sizing: border-box; }
  html, body {
    width: 1200px; height: 768px; overflow: hidden;
    background: var(--backdrop);
    font-family: "Montserrat", Arial, sans-serif;
  }
  .canvas {
    width: 1200px; height: 768px;
    display: flex; align-items: center; justify-content: center; gap: 60px;
  }
  .card {
    width: 520px; height: 298px; border-radius: 20px;
    position: relative; overflow: hidden;
    box-shadow: 0 6px 18px rgba(0,0,0,0.18);
  }
  /* Front */
  .card-front {
    background: var(--card-white);
    display: flex; flex-direction: column; align-items: center; justify-content: center;
  }
  .brand {
    display: flex; align-items: center; gap: 10px;
    color: var(--copper); font-weight: 600; letter-spacing: 0.04em;
  }
  .brand-dot { border-radius: 50%; background: var(--copper); }
  .card-front .brand { font-size: 34px; }
  .card-front .brand-dot { width: 22px; height: 22px; }
  .front-web {
    margin-top: 46px; font-size: 14px; font-weight: 600;
    letter-spacing: 0.28em; color: var(--taupe);
  }
  /* Back */
  .card-back { background: var(--card-black); color: var(--ink-white); }
  .card-back .brand {
    position: absolute; left: 30px; top: 30px; font-size: 18px;
  }
  .card-back .brand-dot { width: 12px; height: 12px; }
  .contact-block { position: absolute; left: 262px; top: 96px; }
  .person-name {
    font-family: "Dancing Script", cursive; font-size: 30px;
    color: var(--copper); line-height: 1;
  }
  .person-title { font-size: 13px; color: var(--soft-grey); margin: 4px 0 12px; }
  .address { font-size: 14px; line-height: 1.3; margin-bottom: 10px; }
  .contact-list { list-style: none; font-size: 14px; }
  .contact-list li { display: flex; align-items: center; gap: 10px; line-height: 1.45; }
  .icon { width: 12px; height: 12px; flex: none; }
</style>
</head>
<body>
<main class="canvas">
  <section class="card card-front">
    <div class="brand"><span class="brand-dot"></span>Hushed Hours</div>
    <p class="front-web">www.HushedHours.com</p>
  </section>

  <section class="card card-back">
    <div class="brand"><span class="brand-dot"></span>Hushed Hours</div>
    <div class="contact-block">
      <h1 class="person-name">Dana Whitfield</h1>
      <p class="person-title">Chief of Staff</p>
      <p class="address">218 Linden Ave, Suite 12<br>Brookfield, OH 44403</p>
      <ul class="contact-list">
        <li>
          <svg class="icon" viewBox="0 0 12 12" fill="#9c9794"><path d="M2.5 1 L4.5 1 L5 3.5 L3.8 4.5 Q5 7 7.5 8.2 L8.5 7 L11 7.5 L11 9.5 Q10.5 11 9 11 Q1 10 1 3 Q1 1.5 2.5 1Z"/></svg>
          (555)014-2290
        </li>
        <li>
          <svg class="icon" viewBox="0 0 12 12" fill="none" stroke="#9c9794" stroke-width="1.2"><rect x="1" y="2.5" width="10" height="7"/><path d="M1 2.5 L6 6.5 L11 2.5"/></svg>
          Dana@HushedHours.com
        </li>
        <li>
          <svg class="icon" viewBox="0 0 12 12" fill="none" stroke="#9c9794" stroke-width="1.1"><circle cx="6" cy="6" r="5"/><ellipse cx="6" cy="6" rx="2.2" ry="5"/><path d="M1 6 H11"/></svg>
          www.HushedHours.com
        </li>
        <li>
          <svg class="icon" viewBox="0 0 12 12"><circle cx="6" cy="6" r="5.5" fill="#9c9794"/></svg>
          @HushedHours
        </li>
      </ul>
    </div>
  </section>
</main>
</body>
</html>
```